Korvanta

1. We need a four color business card
2. The Front of card needs to include our Logo, Slogan which is "Launching, Expanding & Optimizing Organizations, Individual Name, email, two phone numbers, email, skype address, website address
3. Back of card needs to include the following topics: Start Ups & Business Optimization,Product Acquisition, Destination Product Marketing & Representation,Marketing & Sales, Operations, Training/Education, Digital Marketing, Keynote Addresses/Public Speaking
3. Back of card can not be black as it needs to be a color that people can write on
Industry/Entity Type
Business

```html
<!DOCTYPE html>
<html lang="en">
<head>
<meta charset="utf-8">
<title>Korvanta Solutions – Business Card</title>
<link rel="stylesheet" href="https://fonts.googleapis.com/css2?family=Arimo:wght@400;700&display=swap">
<style>
  :root {
    --page-bg: #d9d9dc;
    --card-black: #0b0c0f;
    --card-black-edge: #1c1e24;
    --blue-deep: #0d4f9e;
    --blue-mid: #1b76c9;
    --blue-light: #38b6e6;
    --brand-blue: #2f7fd0;
    --text-white: #f2f4f7;
    --text-soft: #c9d3de;
    --accent-green: #8cc63f;
  }
  * { box-sizing: border-box; margin: 0; padding: 0; }
  html, body { width: 1200px; height: 900px; overflow: hidden; }
  body {
    background: var(--page-bg);
    font-family: "Arimo", Arial, sans-serif;
    display: flex;
    align-items: center;
    justify-content: center;
    gap: 48px;
  }
  .card {
    position: relative;
    width: 540px;
    height: 310px;
    border-radius: 4px;
    overflow: hidden;
    box-shadow: 0 12px 30px rgba(0,0,0,0.25);
  }

  /* Back of card */
  .card-back {
    background: linear-gradient(160deg, var(--blue-light) 0%, var(--blue-mid) 45%, var(--blue-deep) 100%);
    color: var(--text-white);
    padding: 48px 36px 0;
    text-align: center;
  }
  .brand {
    display: inline-flex;
    align-items: center;
    gap: 12px;
  }
  .brand-dot {
    width: 34px; height: 34px;
    border-radius: 50%;
    background: var(--accent-green);
  }
  .brand-text { text-align: left; }
  .brand-name {
    font-size: 36px;
    font-weight: 700;
    line-height: 1;
    letter-spacing: -0.5px;
  }
  .brand-sub {
    font-size: 10px;
    letter-spacing: 7px;
    margin-top: 3px;
  }
  .card-back .brand-name, .card-back .brand-sub { color: var(--text-white); }
  .card-back .slogan-small {
    font-size: 9px;
    font-weight: 700;
    letter-spacing: 1px;
    margin-top: 3px;
  }
  .services {
    list-style: none;
    margin-top: 34px;
    font-size: 15px;
    line-height: 1.45;
  }

  /* Front of card */
  .card-front {
    background: radial-gradient(circle at 70% 30%, var(--card-black-edge) 0%, var(--card-black) 65%);
    color: var(--text-white);
    padding: 30px 30px 0;
  }
  .card-front .brand-name { color: var(--brand-blue); font-size: 34px; }
  .card-front .brand-sub { color: var(--brand-blue); }
  .card-front .brand-dot { background: var(--brand-blue); width: 30px; height: 30px; }
  .deco-circle {
    position: absolute;
    right: 28px; top: 22px;
    width: 150px; height: 150px;
  }
  .person {
    margin-top: 18px;
    font-size: 16px;
    color: var(--brand-blue);
  }
  .person .role { color: var(--text-white); }
  .address {
    margin-top: 10px;
    font-size: 14px;
    line-height: 1.25;
  }
  .contacts {
    margin-top: 10px;
    font-size: 14px;
    line-height: 1.25;
    display: grid;
    grid-template-columns: 62px auto;
  }
  .contacts dt { color: var(--brand-blue); }
  .slogan {
    position: absolute;
    left: 30px; right: 30px; bottom: 18px;
    font-size: 15px;
    font-weight: 700;
    letter-spacing: 0.5px;
    color: var(--brand-blue);
    text-align: right;
    text-transform: uppercase;
  }
</style>
</head>
<body>

  <section class="card card-back" aria-label="Back of business card">
    <div class="brand">
      <span class="brand-dot"></span>
      <div class="brand-text">
        <div class="brand-name">Korvanta</div>
        <div class="brand-sub">SOLUTIONS</div>
        <div class="slogan-small">LAUNCHING, EXPANDING &amp; OPTIMIZING ORGANIZATIONS</div>
      </div>
    </div>
    <ul class="services">
      <li>Start Ups &amp; Business Optimization.Product Acquisition</li>
      <li>Branding.Destination/Product Marketing.Marketing/Sales/Operations</li>
      <li>SEO/SEM &amp; Digital Marketing.Education/Training</li>
      <li>Keynote.Presentations/Seminars/Public Speaking</li>
    </ul>
  </section>

  <section class="card card-front" aria-label="Front of business card">
    <svg class="deco-circle" viewBox="0 0 150 150" aria-hidden="true">
      <circle cx="75" cy="75" r="72" fill="#1a1c22"/>
    </svg>
    <div class="brand">
      <span class="brand-dot"></span>
      <div class="brand-text">
        <div class="brand-name">Korvanta</div>
        <div class="brand-sub">SOLUTIONS</div>
      </div>
    </div>
    <p class="person">Your Name <span class="divider">|</span> <span class="role">Owner</span></p>
    <p class="address">1364 Route Dummy<br>Text, NY Road 12033</p>
    <dl class="contacts">
      <dt>Office:</dt><dd>101-101-1010</dd>
      <dt>Cell:</dt><dd>101-101-1010</dd>
      <dt>Email:</dt><dd>jmarlow@korvanta.com</dd>
      <dt>Skype:</dt><dd>korvanta.team</dd>
      <dt>Web:</dt><dd>www.korvanta.com</dd>
    </dl>
    <p class="slogan">Launching, Expanding &amp; Optimizing Organizations</p>
  </section>

</body>
</html>
```